New Web-Page Design Required

We need a new or initial web design for our page vorlan-grid.com. We provide products & services around infrastructure products. We have two products at the moment, but another 2 in the pipeline.
We want to have the following page structure (and part of the project is to design the 7 pages):
- Home
- Products
-One page per product
- Service
- Support
- About
- Contact (Email form)
The start page should include the following information:
- Twitter / Linkedin Links
- Telephone / Email or in general contact details
- News
- Maybe a link-box, where we can highlight/showcase things
- Link to our support portal, quite prominent
- Testimonials
It would be nice if the product pages would have a image header, where we can put up a screenshot or something. Links to datasheet and videos of the product would be nice as well.
We like the "big banner in the middle" designs, like these two Joomla examples. No need to copy them, it should just give you an idea.
http://www.pelmorthemes.com/itempreview/185
http://www.pelmorthemes.com/content/asj42/index.php
Budget for images available, so please use placeholders or ask us for specific photos/images, if you need them for your design.
Target Market(s)
Business-2-Business, Decision makers and Technical Leads
Industry/Entity Type
News
Look and feel

```html
<!DOCTYPE html>
<html lang="en">
<head>
<meta charset="utf-8">
<title>Vorlan-Grid</title>
<link href="https://fonts.googleapis.com/css2?family=Arimo:wght@400;700&family=Andika&display=swap" rel="stylesheet">
<style>
:root{
  --nav-bg:#e9e9e9;
  --nav-text:#8a8a8a;
  --brand:#1b8fa3;
  --brand-dark:#2d3d48;
  --green:#4caf1a;
  --green-dark:#3f9414;
  --heading:#8c8c8c;
  --body:#6f6f6f;
  --rule:#d9d9d9;
  --box:#e4e4e4;
  --link:#2aa0d8;
  --white:#ffffff;
  --social:#d3d3d3;
}
*{margin:0;padding:0;box-sizing:border-box}
h1,h2,h3{font-weight:400}
html,body{width:867px;height:1200px;overflow:hidden;background:var(--white)}
body{position:relative;font-family:"Arimo",Arial,sans-serif;color:var(--body)}
.abs{position:absolute}

.site-nav{left:0;top:0;width:867px;height:45px;background:var(--nav-bg)}
.brand{left:110px;top:6px;display:flex;align-items:center;gap:7px}
.brand-dot{width:35px;height:35px;border-radius:50%;background:var(--brand)}
.brand-name{font-size:24px;font-weight:700;color:var(--brand-dark)}
.menu{right:44px;top:15px;display:flex;font-size:14px;font-weight:700;color:var(--nav-text)}
.menu span{padding:0 17px}
.menu .sep{padding:0}

.hero{left:0;top:45px;width:867px;height:292px;
  background:radial-gradient(ellipse at 15% 60%,#8a5a33 0%,transparent 55%),
             radial-gradient(ellipse at 75% 45%,#8e7d86 0%,transparent 55%),
             radial-gradient(ellipse at 55% 80%,#5b3e4d 0%,transparent 50%),
             linear-gradient(90deg,#6a4a33,#8b6f5c 45%,#7f6a78 75%,#b9b3b8)}
.hero-title{left:107px;top:123px;font-size:28px;color:var(--white);letter-spacing:-1.2px}
.hero-sub{left:120px;top:159px;width:400px;text-align:center;font-size:14.5px;line-height:24px;color:var(--white)}
.hero-btn{left:109px;top:240px;width:195px;height:41px;border-radius:3px;
  background:linear-gradient(var(--green),var(--green-dark));color:var(--white);
  font-size:16px;font-weight:700;display:flex;align-items:center;justify-content:center}

.feature-box{width:179px;height:81px;border:4px solid #f3f3f3;background:var(--box);
  display:flex;align-items:center;justify-content:center}
.feature-title{font-size:24px;color:var(--heading);text-align:center;width:200px}
.feature-text{font-size:10.5px;line-height:17.7px;color:var(--body);width:150px}

.rule{height:1px;background:var(--rule)}
.band{background:var(--green);color:var(--white);font-weight:700;font-size:22px;
  display:flex;align-items:center;justify-content:center}

.about-title{left:0;width:867px;top:743px;text-align:center;font-size:23px;color:var(--heading)}
.quote-mark{font-size:42px;color:#d8d8d8;font-family:Georgia,serif;line-height:1}
.about-text{left:150px;top:790px;width:584px;text-align:center;font-size:8.6px;line-height:14.5px;color:var(--body)}

.tweets-title{left:129px;top:983px;font-family:"Andika",sans-serif;font-size:13px;color:#333}
.tweet{left:130px;width:178px;height:50px;border-bottom:1px dotted #cfcfcf;font-size:8.6px;line-height:12.6px}
.tweet-dot{position:absolute;left:0;top:2px;width:15px;height:12px;border-radius:50%;background:#444}
.tweet-dot.alt{background:var(--link)}
.tweet-body{position:absolute;left:23px;top:2px}
.tweet-body a{color:var(--link);text-decoration:none}
.tweet-body em{color:#555}

.contact-title{left:366px;top:981px;font-size:15px;color:#111}
.contact-intro{left:369px;top:1009px;font-size:8.4px;color:var(--body)}
.contact-list{left:369px;top:1030px;font-size:9.6px;line-height:16px;color:var(--body)}
.contact-list b{color:#666}
.socials{left:365px;top:1100px;display:flex;gap:7px}
.social{width:28px;height:28px;border-radius:50%;background:var(--social)}

.footer{left:49px;top:1166px;font-size:9.4px;line-height:16px;color:#666}
</style>
</head>
<body>

<header class="abs site-nav">
  <div class="abs brand"><span class="brand-dot"></span><span class="brand-name">vorlan-grid</span></div>
  <nav class="abs menu">
    <span>Home</span><span class="sep">|</span>
    <span>Services</span><span class="sep">|</span>
    <span>Products</span><span class="sep">|</span>
    <span>Support</span><span class="sep">|</span>
    <span>Contact</span>
  </nav>
</header>

<section class="abs hero" role="img" aria-label="Blurred office background photograph"></section>
<h1 class="abs hero-title">We Commit To What Others Walk Away From</h1>
<p class="abs hero-sub">Infrastructure Design (Cluster vs. Non Cluster, Security,<br>Uptime considerations)</p>
<div class="abs hero-btn">VIEW OUR PRODUCTS</div>

<section class="features">
  <div class="abs feature-box" style="left:115px;top:387px">
    <svg width="34" height="32" viewBox="0 0 34 32"><rect x="1" y="2" width="32" height="22" rx="1" fill="#fff"/><rect x="14" y="24" width="6" height="4" fill="#fff"/><rect x="8" y="28" width="18" height="2" fill="#fff"/></svg>
  </div>
  <div class="abs feature-box" style="left:342px;top:387px">
    <svg width="40" height="34" viewBox="0 0 40 34" fill="none" stroke="#fff" stroke-width="2.5"><path d="M12 12 L20 2 L28 12"/><path d="M2 12 H38 L34 32 H6 Z" fill="#fff" stroke="none"/><path d="M12 16 V28 M20 16 V28 M28 16 V28" stroke="#e4e4e4"/></svg>
  </div>
  <div class="abs feature-box" style="left:571px;top:387px">
    <svg width="42" height="42" viewBox="0 0 42 42" fill="none" stroke="#fff" stroke-width="2"><circle cx="21" cy="21" r="19"/><path d="M21 21 L27 10"/><path d="M21 5 V9 M5 21 H9 M33 21 H37 M10 10 L13 13 M32 10 L29 13"/></svg>
  </div>

  <h2 class="abs feature-title" style="left:103px;top:488px">Products</h2>
  <h2 class="abs feature-title" style="left:327px;top:488px">Support</h2>
  <h2 class="abs feature-title" style="left:561px;top:488px">Service</h2>

  <p class="abs feature-text" style="left:133px;top:526px">Our understanding for customer needs combined with our soft­ware development experience, enables us to provide products of outstanding quality.</p>
  <p class="abs feature-text" style="left:361px;top:526px">Our support portal is available 24/7 and personalized support packages can be tailored to your needs.</p>
  <p class="abs feature-text" style="left:592px;top:526px">Installation &amp; Professional Ser­vices can be provided by us or competent partners. In any case, you will get very experi­enced software consultants, who can fix every issue.</p>
</section>

<section class="about">
  <div class="abs rule" style="left:121px;top:703px;width:199px"></div>
  <div class="abs band" style="left:336px;top:689px;width:197px;height:28px">About Us</div>
  <div class="abs rule" style="left:546px;top:703px;width:199px"></div>
  <h2 class="abs about-title">We Commit To What Others Walk Away From</h2>
  <span class="abs quote-mark" style="left:120px;top:766px">&ldquo;</span>
  <p class="abs about-text">Vorlan-Grid was born from a solid infrastructure, management, automation and highly secure environment experience. With software architecture, design, coding and testing that reaches a combined 30+years experience for a young company. Lessons learned including what not to do.<br>Our objective is to be a software development house that designs applications using the latest available technologies and coding it on the same basis, focusing primarily on native mobile applications and the integration of these into different enterprise back end systems</p>
  <span class="abs quote-mark" style="left:677px;top:832px">&rdquo;</span>
</section>

<section class="contact">
  <div class="abs rule" style="left:113px;top:946px;width:225px"></div>
  <div class="abs band" style="left:361px;top:933px;width:143px;height:28px">Get In Touch</div>
  <div class="abs rule" style="left:521px;top:946px;width:224px"></div>

  <h3 class="abs tweets-title">Latest Tweets</h3>
  <div class="abs tweet" style="top:1007px"><span class="tweet-dot"></span><div class="tweet-body">vorlangrid v.Monitor Video:<br><a>vgl.io/KR4mPq7zT2a</a><br><em>24 minutes ago</em></div></div>
  <div class="abs tweet" style="top:1059px"><span class="tweet-dot"></span><div class="tweet-body">vorlangrid v.Monitor Video:<br><a>vgl.io/KR4mPq7zT2a</a><br><em>24 minutes ago</em></div></div>
  <div class="abs tweet" style="top:1109px;border:none"><span class="tweet-dot alt"></span><div class="tweet-body">vorlangrid v.Monitor Video:<br><a>vgl.io/KR4mPq7zT2a</a><br><em>24 minutes ago</em></div></div>

  <h3 class="abs contact-title">Contact</h3>
  <p class="abs contact-intro">Please do not hesitate to get in contact with us:</p>
  <p class="abs contact-list"><b>General Enquiries</b>: info@vorlan-grid.com<br><b>Technical Support</b>: support@vorlan-grid.com<br><b>Product Questions</b>: sales@vorlan-grid.com</p>
  <div class="abs rule" style="left:555px;top:1049px;width:70px;background:none;border-top:1px dotted #cfcfcf"></div>
  <div class="abs rule" style="left:555px;top:1100px;width:70px;background:none;border-top:1px dotted #cfcfcf"></div>
  <div class="abs socials"><span class="social"></span><span class="social"></span><span class="social"></span><span class="social"></span></div>
</section>

<footer class="abs footer">Copyright © 2013 Vorlan-Grid<br>Halbrook, Metriqa are either registered trademarks or trademarks of Halbrook Data Corporation in the United States and/or other countries.</footer>

</body>
</html>
```